Präsentationsvorlagen für Verwaltungsfirma
Zielgruppe
Verwaltungsfirma, IT-Dienstleistungen, Rechnungswesen
Aufgabenstellung
Benötigen Powerpoint Vorlage im Design unserer Farben. inkl. Logo
Benötige das Power Point Format - .pptx

```html
<!DOCTYPE html>
<html lang="de">
<head>
<meta charset="utf-8">
<title>Präsentationsvorlagen</title>
<link href="https://fonts.googleapis.com/css2?family=Open+Sans:wght@400;600;700;800&display=swap" rel="stylesheet">
<style>
:root{
  --blue:#1f5cab;
  --blue-dark:#17457f;
  --blue-light:#6f9fd6;
  --paper:#f3f3f3;
  --white:#ffffff;
  --ink:#555a61;
  --canvas:#ffffff;
}
*{box-sizing:border-box;margin:0;padding:0}
html,body{width:1183px;height:1200px;overflow:hidden;background:var(--canvas)}
body{font-family:"Open Sans",Arial,sans-serif;color:var(--ink)}
.deck{position:relative;width:1183px;height:1200px;display:grid;
  grid-template-columns:repeat(3,360px);grid-template-rows:repeat(5,203px);
  column-gap:30px;row-gap:35px;padding:22px 21px 23px 22px}
.slide{position:relative;overflow:hidden;background:var(--paper);
  box-shadow:0 3px 8px rgba(0,0,0,.28)}
.abs{position:absolute}
.band{position:absolute;background:var(--blue)}
.ph{position:absolute;background:linear-gradient(135deg,#9fb8d2,#4f74a3)}
.title{position:absolute;font-weight:800;color:var(--blue);text-transform:uppercase;letter-spacing:.2px;line-height:1.05}
.label{display:block;font-size:4.6px;font-weight:700;text-transform:uppercase;margin-bottom:2px}
.copy{position:absolute;font-size:4.6px;line-height:1.45}
.on-blue{color:var(--white)}
.logo{position:absolute;display:flex;align-items:center;gap:3px;font-size:8px;font-weight:700;color:var(--blue)}
.logo i{width:5px;height:5px;background:currentColor;display:block}
.logo.light{color:var(--white)}
.icon{position:absolute;width:9px;height:9px}
</style>
</head>
<body>
<main class="deck">

  <!-- 1 cover -->
  <section class="slide" style="background:var(--blue)">
    <div class="ph" style="left:150px;top:0;width:210px;height:203px;background:linear-gradient(120deg,#2c6cc0,#9cc4ec 60%,#3a79c6)" role="img" aria-label="Foto einer Bürofassade aus Glas"></div>
    <h1 class="title on-blue" style="left:18px;top:62px;font-size:13px;color:var(--white)">Präsentation<br>Slide-Vorlagen</h1>
    <p class="copy on-blue" style="left:18px;top:92px;font-size:5px;font-weight:600">Business Präsentation Template</p>
    <div class="logo light" style="left:18px;top:170px"><i></i>Veltaro</div>
  </section>

  <!-- 2 Einleitung -->
  <section class="slide">
    <h2 class="title" style="left:26px;top:26px;font-size:13px">Einleitung</h2>
    <p class="copy" style="left:26px;top:48px;width:300px">Wir betreuen Verwaltung, IT und Rechnungswesen mit klaren Abläufen. Wir betreuen Verwaltung, IT und Rechnungswesen mit klaren Abläufen.</p>
    <p class="copy" style="left:200px;top:112px;width:126px;text-align:right"><span class="label" style="color:var(--blue)">Unsere Werte</span>Wir betreuen Verwaltung, IT und Rechnungswesen mit klaren Abläufen.</p>
    <div class="logo" style="left:266px;top:168px"><i></i>Veltaro</div>
  </section>

  <!-- 3 Über uns -->
  <section class="slide">
    <div class="ph" style="left:0;top:0;width:170px;height:135px;background:linear-gradient(135deg,#8a6a55,#c9a58a 50%,#4e5a6a)" role="img" aria-label="Foto eines lächelnden Teams im Büro"></div>
    <div class="band" style="left:0;top:135px;width:170px;height:68px"></div>
    <h2 class="title" style="left:218px;top:28px;font-size:11px">Über uns</h2>
    <p class="copy" style="left:188px;top:52px;width:74px"><span class="label" style="color:var(--blue)">Überschrift</span>Wir betreuen Verwaltung, IT und Rechnungswesen mit klaren Abläufen.</p>
    <p class="copy" style="left:270px;top:52px;width:74px"><span class="label" style="color:var(--blue)">Überschrift</span>Wir betreuen Verwaltung, IT und Rechnungswesen mit klaren Abläufen.</p>
  </section>

  <!-- 4 Unsere Mission -->
  <section class="slide">
    <div class="logo" style="left:14px;top:14px"><i></i>Veltaro</div>
    <div class="ph" style="left:12px;top:52px;width:96px;height:96px;border-radius:50%;background:linear-gradient(135deg,#c7d6e6,#6f8fb2)" role="img" aria-label="Foto eines Händedrucks"></div>
    <div class="band" style="left:122px;top:0;width:58px;height:203px"></div>
    <p class="copy on-blue" style="left:128px;top:30px;width:48px"><span class="label">Überschrift</span>Wir betreuen Verwaltung, IT und Rechnungswesen mit klaren Abläufen.</p>
    <h2 class="title" style="left:194px;top:36px;font-size:12px">Unsere Mission</h2>
    <p class="copy" style="left:194px;top:60px;width:150px">Wir betreuen Verwaltung, IT und Rechnungswesen mit klaren Abläufen.</p>
  </section>

  <!-- 5 Unsere Vision -->
  <section class="slide">
    <div class="ph" style="left:22px;top:0;width:84px;height:80px;background:linear-gradient(135deg,#6c4a3f,#c8a78f)" role="img" aria-label="Foto einer Nahaufnahme am Arbeitsplatz"></div>
    <div class="ph" style="left:22px;top:84px;width:84px;height:119px;background:linear-gradient(135deg,#5b7ea8,#d6e2ee)" role="img" aria-label="Foto einer technischen Nahaufnahme"></div>
    <div class="band" style="left:106px;top:24px;width:190px;height:150px"></div>
    <h2 class="title on-blue" style="left:116px;top:46px;font-size:13px;color:var(--white)">Unsere Vision</h2>
    <p class="copy on-blue" style="left:116px;top:72px;width:88px"><span class="label">Überschrift</span>Wir betreuen Verwaltung, IT und Rechnungswesen mit klaren Abläufen.</p>
    <p class="copy" style="left:300px;top:28px;width:54px"><span class="label" style="color:var(--blue)">Überschrift</span>Wir betreuen Verwaltung, IT und Rechnungswesen mit klaren Abläufen.</p>
    <div class="logo light" style="left:230px;top:150px"><i></i>Veltaro</div>
  </section>

  <!-- 6 Unser Service -->
  <section class="slide">
    <h2 class="title" style="left:200px;top:24px;font-size:12px">Unser Service</h2>
    <p class="copy" style="left:200px;top:42px;width:120px">Wir betreuen Verwaltung, IT und Rechnungswesen mit klaren Abläufen.</p>
    <p class="copy" style="left:30px;top:60px;width:150px"><span class="label" style="color:var(--blue)">Überschrift</span>Wir betreuen Verwaltung, IT und Rechnungswesen mit klaren Abläufen.</p>
    <p class="copy" style="left:30px;top:100px;width:150px"><span class="label" style="color:var(--blue)">Überschrift</span>Wir betreuen Verwaltung, IT und Rechnungswesen mit klaren Abläufen.</p>
    <svg class="icon" style="left:335px;top:28px" viewBox="0 0 10 10"><path d="M1 1 9 9M9 1 1 9" stroke="#333" stroke-width="1.4"/></svg>
    <svg class="icon" style="left:335px;top:48px" viewBox="0 0 10 10"><path d="M1 3h7l-2-2M9 7H2l2 2" fill="none" stroke="#333" stroke-width="1.2"/></svg>
    <div class="ph" style="left:200px;top:132px;width:160px;height:71px;background:linear-gradient(135deg,#8c96a6,#d2d8e0)" role="img" aria-label="Foto einer Besprechung am Tisch"></div>
  </section>

  <!-- 7 Unser Service 2 -->
  <section class="slide">
    <div class="ph" style="left:0;top:0;width:88px;height:68px;background:linear-gradient(135deg,#aab7c7,#52698a)" role="img" aria-label="Foto von Händen, die Puzzleteile halten"></div>
    <div class="band" style="left:0;top:68px;width:88px;height:40px"></div>
    <svg class="icon" style="left:96px;top:20px" viewBox="0 0 10 10"><circle cx="5" cy="5" r="4.5" fill="#1f5cab"/><path d="M3 5h4M5 3l2 2-2 2" stroke="#fff" stroke-width="1" fill="none"/></svg>
    <svg class="icon" style="left:96px;top:60px" viewBox="0 0 10 10"><path d="M1 3h7l-2-2M9 7H2l2 2" fill="none" stroke="#333" stroke-width="1.2"/></svg>
    <p class="copy" style="left:110px;top:18px;width:60px"><span class="label" style="color:var(--blue)">Überschrift</span>Wir betreuen Verwaltung, IT und Rechnungswesen mit klaren Abläufen.</p>
    <p class="copy" style="left:110px;top:58px;width:60px"><span class="label" style="color:var(--blue)">Überschrift</span>Wir betreuen Verwaltung, IT und Rechnungswesen mit klaren Abläufen.</p>
    <h2 class="title" style="left:200px;top:30px;font-size:12px">Unser Service</h2>
    <div class="band" style="left:196px;top:46px;width:164px;height:6px"></div>
    <div class="ph" style="left:196px;top:110px;width:164px;height:93px;background:linear-gradient(135deg,#2b6fc9,#8fbdf0)" role="img" aria-label="Foto von blauen Puzzleteilen"></div>
    <div class="logo" style="left:14px;top:170px"><i></i>Veltaro</div>
  </section>

  <!-- 8 Lösungen -->
  <section class="slide">
    <h2 class="title" style="left:22px;top:28px;font-size:12px">Lösungen</h2>
    <p class="copy" style="left:22px;top:46px;width:150px">Wir betreuen Verwaltung, IT und Rechnungswesen mit klaren Abläufen.</p>
    <div class="band" style="left:0;top:96px;width:216px;height:66px"></div>
    <p class="copy on-blue" style="left:22px;top:106px;width:150px"><span class="label">Überschrift</span>Wir betreuen Verwaltung, IT und Rechnungswesen mit klaren Abläufen.</p>
    <div class="ph" style="left:216px;top:0;width:144px;height:203px;background:linear-gradient(160deg,#ffffff,#e4e8ee 55%,#3b4656)" role="img" aria-label="Foto einer Hand mit blauem Puzzleteil"></div>
  </section>

  <!-- 9 Lösungen 2 -->
  <section class="slide">
    <div class="band" style="left:166px;top:0;width:194px;height:50px"></div>
    <p class="copy on-blue" style="left:178px;top:10px;width:160px"><span class="label">Überschrift</span>Wir betreuen Verwaltung, IT und Rechnungswesen mit klaren Abläufen.</p>
    <div class="ph" style="left:16px;top:30px;width:140px;height:86px;background:radial-gradient(circle at 50% 50%,#4fb3e8,#0d2b4a 70%)" role="img" aria-label="Foto einer digitalen Linse"></div>
    <div class="ph" style="left:166px;top:56px;width:178px;height:86px;background:linear-gradient(135deg,#3a1f6e,#c84fc2 50%,#1e5fb8)" role="img" aria-label="Foto einer beleuchteten Computerplatine"></div>
    <h2 class="title" style="left:16px;top:126px;font-size:12px">Lösungen</h2>
    <p class="copy" style="left:16px;top:144px;width:140px">Wir betreuen Verwaltung, IT und Rechnungswesen mit klaren Abläufen.</p>
  </section>

  <!-- 10 Our Product -->
  <section class="slide">
    <div class="ph" style="left:22px;top:0;width:120px;height:203px;background:linear-gradient(135deg,#6f8aa8,#b7c6d6 50%,#3f5873)" role="img" aria-label="Foto eines Büros mit Glaswänden"></div>
    <div class="band" style="left:0;top:96px;width:160px;height:56px"></div>
    <p class="copy on-blue" style="left:14px;top:104px;width:120px"><span class="label">Überschrift</span>Wir betreuen Verwaltung, IT und Rechnungswesen mit klaren Abläufen.</p>
    <h2 class="title" style="left:224px;top:50px;font-size:14px;text-transform:none">Our Product</h2>
    <p class="copy" style="left:184px;top:74px;width:160px">Wir betreuen Verwaltung, IT und Rechnungswesen mit klaren Abläufen.</p>
    <div class="logo" style="left:14px;top:170px"><i></i>Veltaro</div>
  </section>

  <!-- 11 Projekte -->
  <section class="slide">
    <h2 class="title" style="left:50px;top:20px;font-size:10px">Projekte</h2>
    <div class="ph" style="left:46px;top:42px;width:110px;height:161px;background:radial-gradient(circle at 50% 45%,#7fc6f0,#2a5f96 50%,#1a2f4a)" role="img" aria-label="Foto einer Hand mit digitaler Netzwerkgrafik"></div>
    <p class="copy" style="left:170px;top:30px;width:170px">Wir betreuen Verwaltung, IT und Rechnungswesen mit klaren Abläufen.</p>
    <div class="band" style="left:110px;top:106px;width:250px;height:74px"></div>
    <p class="copy on-blue" style="left:176px;top:118px;width:160px"><span class="label">Überschrift</span>Wir betreuen Verwaltung, IT und Rechnungswesen mit klaren Abläufen.</p>
  </section>

  <!-- 12 Foto Folie -->
  <section class="slide" style="background:#1b1440">
    <div class="ph" style="left:0;top:0;width:360px;height:203px;background:linear-gradient(120deg,#2a1b6e,#7a3fd0 35%,#1f7ee0 60%,#5a1e9c 85%,#140c33)" role="img" aria-label="Foto mit abstrakten violetten und blauen Lichtlinien"></div>
    <p class="copy on-blue" style="left:20px;top:30px;width:120px"><span class="label">Überschrift</span>Wir betreuen Verwaltung, IT und Rechnungswesen mit klaren Abläufen.</p>
    <h2 class="title" style="left:232px;top:66px;font-size:30px;color:var(--white);line-height:1">Foto<br>Folie</h2>
    <div class="logo light" style="left:20px;top:170px"><i></i>Veltaro</div>
  </section>

  <!-- 13 Unser Team -->
  <section class="slide">
    <div class="ph" style="left:22px;top:14px;width:110px;height:189px;background:linear-gradient(180deg,#dfe3e8,#8390a0 60%,#3d4656)" role="img" aria-label="Foto einer Gruppe im Businessoutfit"></div>
    <h2 class="title" style="left:150px;top:66px;font-size:13px">Unser Team</h2>
    <p class="copy" style="left:150px;top:84px;width:100px;font-weight:700;color:var(--blue);text-transform:uppercase">Business Präsentation Template</p>
    <div class="band" style="left:150px;top:110px;width:180px;height:46px"></div>
    <p class="copy on-blue" style="left:160px;top:120px;width:160px">Wir betreuen Verwaltung, IT und Rechnungswesen mit klaren Abläufen.</p>
  </section>

  <!-- 14 Team -->
  <section class="slide">
    <div class="ph" style="left:22px;top:14px;width:38px;height:38px;background:linear-gradient(135deg,#c9ccd2,#6d7787)" role="img" aria-label="Porträtfoto Teammitglied"></div>
    <div class="ph" style="left:64px;top:14px;width:38px;height:38px;background:linear-gradient(135deg,#d6d8dc,#7b8595)" role="img" aria-label="Porträtfoto Teammitglied"></div>
    <div class="ph" style="left:22px;top:58px;width:38px;height:38px;background:linear-gradient(135deg,#c2c6cc,#5f6a7a)" role="img" aria-label="Porträtfoto Teammitglied"></div>
    <div class="ph" style="left:64px;top:58px;width:38px;height:38px;background:linear-gradient(135deg,#d0d3d8,#717b8b)" role="img" aria-label="Porträtfoto Teammitglied"></div>
    <div class="ph" style="left:22px;top:102px;width:38px;height:38px;background:linear-gradient(135deg,#c7cad0,#66707f)" role="img" aria-label="Porträtfoto Teammitglied"></div>
    <div class="ph" style="left:64px;top:102px;width:38px;height:38px;background:linear-gradient(135deg,#d3d6da,#7a8494)" role="img" aria-label="Porträtfoto Teammitglied"></div>
    <div class="ph" style="left:22px;top:146px;width:38px;height:38px;background:linear-gradient(135deg,#c5c9cf,#636d7c)" role="img" aria-label="Porträtfoto Teammitglied"></div>
    <div class="ph" style="left:64px;top:146px;width:38px;height:38px;background:linear-gradient(135deg,#cfd2d7,#737d8c)" role="img" aria-label="Porträtfoto Teammitglied"></div>
    <h2 class="title" style="left:280px;top:40px;font-size:13px">Team</h2>
    <p class="copy" style="left:150px;top:62px;width:190px">Wir betreuen Verwaltung, IT und Rechnungswesen mit klaren Abläufen.</p>
    <div class="band" style="left:120px;top:108px;width:222px;height:56px"></div>
    <p class="copy on-blue" style="left:134px;top:118px;width:190px"><span class="label">Überschrift</span>Wir betreuen Verwaltung, IT und Rechnungswesen mit klaren Abläufen.</p>
  </section>

  <!-- 15 Dankeschön -->
  <section class="slide">
    <p class="copy" style="left:0;top:76px;width:360px;text-align:center"><span class="label" style="color:var(--blue)">Überschrift</span></p>
    <h2 class="title" style="left:0;top:88px;width:360px;text-align:center;font-size:26px">Dankeschön</h2>
    <div class="logo" style="left:152px;top:124px"><i></i>Veltaro</div>
  </section>

</main>
</body>
</html>
```